New business card for civil engineering company - "Keystone Audit"

We need a business card designed for our new structural engineering company.

The company name is "Keystone Audit" logo files attached.

We would like the following:
* Two-sided card
* Simple design

Information to be placed on the card:
Name - Marcus Dellow
Job Title - Director / Structural Engineer
Credentials - BEng(Hons), CPEng, CMengNZ, IntPE(NZ)
Email - marcus.dellow@keystoneaudit.co.nz
mobile - 0219364058
website - www.keystoneaudit.co.nz

```html
<!DOCTYPE html>
<html lang="en">
<head>
<meta charset="utf-8">
<title>Keystone Audit – Business Card</title>
<link href="https://fonts.googleapis.com/css2?family=Roboto:wght@400;500;700&display=swap" rel="stylesheet">
<style>
  :root {
    --canvas: #e4e4e4;
    --white: #ffffff;
    --sky: #86c2ea;
    --azure: #3f88c9;
    --azure-light: #4f97d2;
    --navy-top: #0c5583;
    --navy-bottom: #053f6d;
    --ink: #3d3d3d;
  }
  * { margin: 0; padding: 0; box-sizing: border-box; }
  html, body { width: 1200px; height: 1200px; overflow: hidden; }
  body {
    background: var(--canvas);
    font-family: "Roboto", Arial, sans-serif;
    position: relative;
  }
  .card {
    position: absolute;
    left: 160px;
    width: 880px;
    height: 503px;
    overflow: hidden;
  }
  .card--front { top: 57px; background: var(--white); }
  .card--back {
    top: 640px;
    background: linear-gradient(180deg, var(--navy-top), var(--navy-bottom));
  }
  .card__shapes { position: absolute; inset: 0; width: 100%; height: 100%; }

  .brand {
    position: absolute;
    display: flex;
    align-items: center;
    gap: 12px;
    font-weight: 500;
    text-transform: uppercase;
    letter-spacing: 0.12em;
    white-space: nowrap;
  }
  .brand__square { width: 18px; height: 18px; flex: none; }
  .card--front .brand {
    left: 271px; top: 215px; transform: translateX(-50%);
    font-size: 30px; color: var(--ink);
  }
  .card--front .brand__square { background: var(--azure); }
  .card--back .brand {
    left: 50%; top: 50%; transform: translate(-50%, -50%);
    font-size: 40px; color: var(--white);
  }
  .card--back .brand__square { width: 22px; height: 22px; background: #2a7fbf; }

  .contact {
    position: absolute;
    right: 45px;
    top: 290px;
    text-align: right;
    color: var(--white);
  }
  .contact__name { font-size: 28px; font-weight: 700; line-height: 1.1; }
  .contact__credentials { font-size: 17.5px; line-height: 1.3; }
  .contact__role { font-size: 20px; line-height: 1.4; margin-bottom: 14px; }
  .contact__list { list-style: none; }
  .contact__item {
    display: flex; justify-content: flex-end; align-items: center;
    gap: 12px; font-size: 20px; line-height: 25px;
  }
  .contact__icon { width: 15px; height: 15px; flex: none; fill: var(--white); }
</style>
</head>
<body>

<section class="card card--front" aria-label="Business card front">
  <svg class="card__shapes" viewBox="0 0 800 457" preserveAspectRatio="none" aria-hidden="true">
    <polygon points="0,254 0,457 330,457" fill="var(--sky)"/>
    <defs>
      <linearGradient id="band" x1="0" y1="0" x2="0" y2="1">
        <stop offset="0" stop-color="var(--azure-light)"/>
        <stop offset="1" stop-color="var(--azure)"/>
      </linearGradient>
    </defs>
    <polygon points="800,47 800,457 330,457 256,410" fill="url(#band)"/>
  </svg>

  <div class="brand"><span class="brand__square"></span>Keystone Audit</div>

  <div class="contact">
    <p class="contact__name">Marcus Dellow BEng</p>
    <p class="contact__credentials">(Hons), CPEng, CMengNZ, IntPE(NZ)</p>
    <p class="contact__role">Director / Structural Engineer</p>
    <ul class="contact__list">
      <li class="contact__item">0219364058
        <svg class="contact__icon" viewBox="0 0 24 24" aria-hidden="true"><path d="M6.6 10.8a15.1 15.1 0 0 0 6.6 6.6l2.2-2.2c.3-.3.7-.4 1-.2 1.1.4 2.3.6 3.6.6.6 0 1 .4 1 1V20c0 .6-.4 1-1 1A17 17 0 0 1 3 4c0-.6.4-1 1-1h3.5c.6 0 1 .4 1 1 0 1.3.2 2.5.6 3.6.1.3 0 .7-.2 1z"/></svg>
      </li>
      <li class="contact__item">marcus.dellow@keystoneaudit.co.nz
        <svg class="contact__icon" viewBox="0 0 24 24" aria-hidden="true"><path d="M2 5h20v14H2z M3.5 6.5 12 13l8.5-6.5" fill="var(--white)" stroke="var(--azure)" stroke-width="1.6"/></svg>
      </li>
      <li class="contact__item">www.keystoneaudit.co.nz
        <svg class="contact__icon" viewBox="0 0 24 24" aria-hidden="true"><circle cx="12" cy="12" r="10"/><path d="M2 12h20M12 2c3 3 3 17 0 20M12 2c-3 3-3 17 0 20" fill="none" stroke="var(--azure)" stroke-width="1.5"/></svg>
      </li>
    </ul>
  </div>
</section>

<section class="card card--back" aria-label="Business card back">
  <div class="brand"><span class="brand__square"></span>Keystone Audit</div>
</section>

</body>
</html>
```